harvest Soon Book Cover Design for real estate investment book

I am looking for a Book Cover design for my new book. I would like designs for a hardcover, softcover and Lumora book.

The book deals with real estate and mortgage investments. Looking for a clean, bright simple design. Want to cover to be White with big RED letters. See "Dancing past Noon" book for an example ... see attached.

Target Market(s)

Affluent people with money looking for investment solutions.

Industry/Entity Type

Financial Service

Font styles to use
Serif

Requirements
Must have
• Bright clean design that will be appealing to affluent people.
• Title: harvest SOON
• Subtitle: A quiet method for thriving through land holdings
• subsubtitle: Secrets the Bank Teller Keeps Hidden From Clients...
• Author: Ned Falconby
• My Picture on the inside cover or on the back cover
• Book Description, Author description
Nice to have
• Focus on the Front cover look and feel first. Then we can look at the inside flaps and back cover. I will need to send you text. This is for the full cover. Front. Back. Spine. Inside flaps fro hardcover.

```html
<!DOCTYPE html>
<html lang="en">
<head>
<meta charset="utf-8">
<title>harvest SOON — Ned Falconby</title>
<link rel="stylesheet" href="https://fonts.googleapis.com/css2?family=Roboto+Condensed:wght@400;700&family=Archivo+Black&display=swap">
<style>
  :root {
    --paper: #f4f4f4;
    --paper-edge: #d9d9d9;
    --ink: #1a1a1a;
    --red: #d9202a;
    --red-title: rgba(214, 24, 36, 0.93);
    --white: #ffffff;
    --photo-light: #e6e6e6;
    --photo-mid: #9a9a9a;
    --photo-dark: #3b3b3b;
  }
  * { margin: 0; padding: 0; box-sizing: border-box; }
  html, body { width: 846px; height: 1200px; overflow: hidden; background: var(--paper); }
  .cover {
    position: relative;
    width: 846px;
    height: 1200px;
    overflow: hidden;
    background: radial-gradient(ellipse at 45% 40%, #ffffff 0%, var(--paper) 45%, var(--paper-edge) 100%);
    font-family: "Roboto Condensed", "Arial Narrow", sans-serif;
    color: var(--ink);
  }
  .kicker {
    position: absolute;
    left: 112px;
    top: 86px;
    font-size: 31px;
    line-height: 36px;
    font-weight: 400;
    letter-spacing: -0.2px;
  }
  .hero-photo {
    position: absolute;
    left: 110px;
    top: 300px;
    width: 736px;
    height: 740px;
    background:
      radial-gradient(ellipse 28% 22% at 42% 28%, var(--photo-mid) 0%, rgba(154,154,154,0) 100%),
      radial-gradient(ellipse 48% 8% at 42% 54%, rgba(190,190,190,0.9) 0%, rgba(190,190,190,0) 100%),
      radial-gradient(ellipse 30% 38% at 95% 85%, var(--photo-dark) 0%, rgba(59,59,59,0) 100%);
  }
  .title {
    position: absolute;
    left: 0;
    top: 0;
    width: 846px;
    height: 600px;
  }
  .title text {
    font-family: "Archivo Black", "Arial Black", sans-serif;
    fill: var(--red-title);
  }
  .subtitle {
    position: absolute;
    left: 135px;
    top: 762px;
    width: 400px;
    font-size: 38px;
    line-height: 43px;
    font-weight: 400;
    letter-spacing: -0.3px;
  }
  .author-band {
    position: absolute;
    left: 0;
    top: 1032px;
    width: 846px;
    height: 108px;
    background: var(--red);
    display: flex;
    align-items: center;
    padding-left: 135px;
  }
  .author-name {
    color: var(--white);
    font-size: 58px;
    font-weight: 700;
    letter-spacing: 0.5px;
    text-transform: uppercase;
  }
</style>
</head>
<body>
  <main class="cover">
    <p class="kicker">Secrets the Bank Teller Keeps<br>Hidden From Clients...</p>

    <div class="hero-photo" role="img" aria-label="Black-and-white photo of a businessman's open hand in a pinstripe suit sleeve, holding a small city skyline model"></div>

    <svg class="title" viewBox="0 0 846 600" aria-label="harvest SOON">
      <text x="120" y="362" font-size="172" textLength="608" lengthAdjust="spacingAndGlyphs">HARVEST</text>
      <text x="126" y="570" font-size="238" textLength="596" lengthAdjust="spacingAndGlyphs">SOON</text>
    </svg>

    <p class="subtitle">A quiet method for thriving through land holdings</p>

    <div class="author-band">
      <span class="author-name">Ned Falconby</span>
    </div>
  </main>
</body>
</html>
```